Dietary supplement, Clean and simple.

Hi,
I’d like to talk about the project,

About us:
We are a dietary supplement (Vitamins, Minerals, amino acids etc.) company.
The goal is to have about 25 products at the end of this year. However, for this goal to be achieved we need a good label design to make our products represent our company values.
I’ll be here every day supporting your questions, we are fully committed to making the highest/best quality/customer experience possible.

About the design and our values:
- Professional (We are in the industry of professionalism and expertise. I would love to show we are competent at this, Id. Like to have the labels looks like we have done our research.)
- Efficient (White spacing, good use of the space available.)
- Simple (Straight forward, in 5 seconds they have to know what the product they have is/how functions. We’re trying to simplify it for the consumer.
- No distractions (the only visually “distracting” factor can be the vector art.)

The guidelines:
The goal is to have a universal design, with one element that changes (Vector art). I’ll attach a file/multiple files I think can show some visuals on what I’m looking for, and what parts of the design I think are good/bad.

Label size: 69x155mm (Front is 77.5mm)

Design whatever you think fits our image. You’re the design expert, all I care about is that it fits our company standards/image.

Use this color/font.
Font: Sans Serif
Main company color is Mind green #237D62 (Use this color for something in the design.)

What I thought would be cool/might looks ugly, who knows:
1. The front of the label: Should have 1 vector art, preferably in the top right corner. (That looks good in multiple colors. The vector can have multiple areas to color, I would prefer 2 main colors in the vector art. The interchangeable colors are used for multiple kinds of products.)
2. Text/product information on the left. The text that will have to be displayed:
- Product name for instance “Magnesium + B6”
- Description for the product for instance “Magnesium with ginger taste”
- Company name or logo. (Add ® behind it. We are soon to be trademark registered.)
3. We need to show the "daily intake" amount on the front and also the amount in the complete bottle. For instance, “Daily intake 1 capsule, 60 capsules”.
• You don’t have to design the backside of the label. After I chose a design, I’d like to chat and give specific information on what areas need to be assigned where. (Too complex because of the law.)
Updates

Hi, Please make the deadline 31 days total. I want designers to have the time to design. And not be rushed to finish it.

I want to extend the deadline because i feel like a slightly more medical look would be interesting. Hope you can come up with something!!

Target Market(s)

Dietary supplement consumers

Industry/Entity Type

Dietary supplements

Font styles to use
Sans Serif

Colors

Designer to choose colors to be used in the design.

Requirements
Must have
• Trademark icon "®" has to be at the top right after the company logo(text of logo)/name.

```html
<!DOCTYPE html>
<html lang="en">
<head>
<meta charset="utf-8">
<title>Magnesium + B6 Label</title>
<link rel="stylesheet" href="https://fonts.googleapis.com/css2?family=Source+Sans+3:wght@400;600;700&display=swap">
<style>
  :root {
    --page: #ffffff;
    --sage: #88b7a8;
    --mind-green: #237D62;
    --ink: #1f1f1f;
    --mustard: #cfc22c;
    --teal-ring: #2aa1ad;
    --badge-rim: #e6ecec;
  }
  * { margin: 0; padding: 0; box-sizing: border-box; }
  html, body {
    width: 1200px; height: 1200px; overflow: hidden;
    background: var(--page);
    font-family: "Source Sans 3", sans-serif;
  }
  .label {
    position: absolute;
    left: 90px; top: 370px;
    width: 1020px; height: 459px;
    background: var(--sage);
    overflow: hidden;
  }
  .label__disc {
    position: absolute;
    left: 267px; top: -6px;
    width: 471px; height: 471px;
    border-radius: 50%;
    background: #ffffff;
  }
  .brand {
    position: absolute;
    left: 0; width: 1020px; top: 104px;
    text-align: center;
    color: var(--mind-green);
    font-weight: 700;
    font-size: 34px;
    line-height: 1;
    letter-spacing: 0.5px;
  }
  .brand sup { font-size: 14px; vertical-align: top; margin-left: 2px; }
  .product-name {
    position: absolute;
    left: 300px; top: 208px;
    font-size: 48px; font-weight: 600;
    color: var(--ink);
    line-height: 1;
    letter-spacing: 0.3px;
  }
  .product-tagline {
    position: absolute;
    left: 302px; top: 263px;
    height: 28px;
    padding: 0 8px;
    border-radius: 7px;
    background: var(--mustard);
    color: var(--ink);
    font-size: 21px; font-weight: 400;
    line-height: 28px;
    white-space: nowrap;
  }
  .product-type {
    position: absolute;
    left: 385px; top: 358px;
    font-size: 22px; font-weight: 700;
    color: var(--mind-green);
    letter-spacing: 0.3px;
    line-height: 1;
  }
  .count-badge {
    position: absolute;
    left: 622px; top: 277px;
    width: 106px; height: 106px;
  }
  .count-badge__text {
    position: absolute; inset: 0;
    display: flex; flex-direction: column;
    align-items: center; justify-content: center;
    color: var(--ink);
  }
  .count-badge__number { font-size: 38px; font-weight: 700; line-height: 0.9; }
  .count-badge__unit { font-size: 11px; font-weight: 400; letter-spacing: 0.2px; }
</style>
</head>
<body>
  <div class="label">
    <div class="label__disc"></div>

    <div class="brand">Verdant Calm<sup>®</sup></div>

    <h1 class="product-name">MAGNESIUM + B6</h1>
    <p class="product-tagline">Magnesium with ginger taste</p>

    <div class="count-badge">
      <svg width="106" height="106" viewBox="0 0 106 106" aria-hidden="true">
        <defs>
          <radialGradient id="badgeFace" cx="45%" cy="35%" r="70%">
            <stop offset="0" stop-color="#ffffff"/>
            <stop offset="1" stop-color="#dfe5e5"/>
          </radialGradient>
        </defs>
        <ellipse cx="60" cy="96" rx="38" ry="6" fill="#000" opacity="0.08"/>
        <circle cx="53" cy="51" r="51" fill="var(--badge-rim)"/>
        <circle cx="53" cy="51" r="41" fill="var(--teal-ring)"/>
        <circle cx="53" cy="51" r="36" fill="url(#badgeFace)"/>
      </svg>
      <div class="count-badge__text" style="bottom:4px">
        <span class="count-badge__number">60</span>
        <span class="count-badge__unit">CAPSULES</span>
      </div>
    </div>

    <p class="product-type">DIETARY SUPPLEMENT</p>
  </div>
</body>
</html>
```